Business Card for my New Brokerage

Looking to get a business card design for my new Real Estate Brokerage.
I want it with Picture, Phone Number, Email, Website, Office Address
Name and Designation. Please add logo too.

Target Market(s)

Real Estate Investors or Home Buyers

Industry/Entity Type

Real Estate

Contact Information for Business Card

Name, Email, Phone Number, website, email, office address

Colors
EB3D1F
EC4F4E
F09395
F8D3D4
FCEDEE

Requirements
Must have
• Minimalistic, Clean, Modern, Photo
Nice to have
• White and Red Colors

```html
<!DOCTYPE html>
<html lang="en">
<head>
<meta charset="utf-8">
<title>Ember Realty Inc – Business Card</title>
<link rel="stylesheet" href="https://fonts.googleapis.com/css2?family=Montserrat:wght@600&family=Open+Sans:wght@400;700&display=swap">
<style>
  :root {
    --brand-red: #dd1c24;
    --back-red-top: #e0393f;
    --back-red-bottom: #bb1a23;
    --white: #ffffff;
    --paper: #ffffff;
    --photo-sky: #f7f7f7;
    --photo-hills: #9a9a9a;
    --photo-ground: #2e2e2e;
    --shadow: rgba(0, 0, 0, 0.35);
  }
  * { margin: 0; padding: 0; box-sizing: border-box; }
  html, body {
    width: 927px;
    height: 1200px;
    overflow: hidden;
    background: var(--paper);
  }
  .canvas {
    position: relative;
    width: 927px;
    height: 1200px;
  }
  .card {
    position: absolute;
    left: 64px;
    width: 792px;
    box-shadow: 0 10px 28px var(--shadow);
    overflow: hidden;
  }

  /* Front side */
  .card--front {
    top: 111px;
    height: 452px;
    background: var(--white);
  }
  .card__edge {
    position: absolute;
    top: 0;
    width: 14px;
    height: 100%;
    background: var(--brand-red);
  }
  .card__edge--left { left: 0; }
  .card__edge--right { right: 0; }
  .front-photo {
    position: absolute;
    left: 14px;
    right: 14px;
    top: 0;
    bottom: 0;
    background: linear-gradient(180deg,
      var(--photo-sky) 0%,
      var(--photo-sky) 38%,
      var(--photo-hills) 50%,
      #6a6a6a 65%,
      var(--photo-ground) 100%);
  }
  .brand {
    position: absolute;
    left: 0;
    right: 0;
    top: 210px;
    text-align: center;
    font-family: "Montserrat", sans-serif;
    font-weight: 600;
    color: var(--brand-red);
    line-height: 1;
  }
  .brand__name {
    display: block;
    font-size: 62px;
    letter-spacing: 1px;
  }
  .brand__suffix {
    display: block;
    margin-top: 10px;
    font-size: 18px;
    letter-spacing: 5px;
  }

  /* Back side */
  .card--back {
    top: 653px;
    height: 439px;
  }
  .back-photo {
    position: absolute;
    inset: 0;
    background: linear-gradient(180deg, var(--back-red-top) 0%, #d42a31 50%, var(--back-red-bottom) 100%);
  }
  .profile {
    position: absolute;
    left: 95px;
    top: 113px;
    width: 240px;
    text-align: center;
    color: var(--white);
    font-family: "Open Sans", sans-serif;
  }
  .profile__avatar {
    display: block;
    margin: 0 auto;
  }
  .profile__name {
    margin-top: 28px;
    font-size: 29px;
    font-weight: 700;
    line-height: 1;
    white-space: nowrap;
    margin-left: -40px;
    margin-right: -40px;
  }
  .profile__role {
    margin-top: 8px;
    font-size: 21px;
    font-weight: 400;
    line-height: 1;
  }
  .divider {
    position: absolute;
    left: 405px;
    top: 147px;
    width: 1.5px;
    height: 145px;
    background: var(--white);
  }
  .contact-list {
    position: absolute;
    left: 426px;
    top: 144px;
    list-style: none;
    font-family: "Open Sans", sans-serif;
    color: var(--white);
  }
  .contact-list__item {
    display: flex;
    align-items: center;
    height: 41px;
    font-size: 19px;
    letter-spacing: 1px;
    white-space: nowrap;
  }
  .contact-list__item--address { letter-spacing: 0.3px; }
  .contact-list__icon {
    width: 24px;
    height: 24px;
    margin-right: 18px;
    flex: none;
  }
</style>
</head>
<body>
<main class="canvas">

  <section class="card card--front" aria-label="Card front">
    <div class="front-photo" role="img" aria-label="Black and white photo of a turf-roofed farmhouse in an open valley with hills behind"></div>
    <div class="card__edge card__edge--left"></div>
    <div class="card__edge card__edge--right"></div>
    <div class="brand">
      <span class="brand__name">EMBER</span>
      <span class="brand__suffix">REALTY INC</span>
    </div>
  </section>

  <section class="card card--back" aria-label="Card back">
    <div class="back-photo" role="img" aria-label="Red-tinted photo of the farmhouse in the valley"></div>

    <div class="profile">
      <svg class="profile__avatar" width="128" height="128" viewBox="0 0 128 128" fill="none" stroke="#ffffff" stroke-width="3" aria-hidden="true">
        <circle cx="64" cy="64" r="62"/>
        <circle cx="64" cy="50" r="19" stroke-width="5"/>
        <path d="M34 96 Q34 72 50 66 Q64 74 78 66 Q94 72 94 96 Z" stroke-width="5" stroke-linejoin="round"/>
      </svg>
      <div class="profile__name">Daniel J. Whitmore</div>
      <div class="profile__role">Managing Director</div>
    </div>

    <div class="divider"></div>

    <ul class="contact-list">
      <li class="contact-list__item">
        <svg class="contact-list__icon" viewBox="0 0 24 24" aria-hidden="true">
          <path fill="#ffffff" d="M6.6 2.5c.6-.4 1.3-.2 1.6.4l1.8 3.3c.3.6.1 1.2-.4 1.6l-1.3 1c1 2.2 2.7 4 4.9 5.1l1-1.3c.4-.5 1.1-.7 1.6-.4l3.3 1.8c.6.3.8 1 .4 1.6l-1.3 2c-.6.9-1.7 1.3-2.8 1-5.3-1.6-9.3-5.7-10.9-11-.3-1 .1-2.1 1-2.7z"/>
        </svg>
        555 - 204 - 3187
      </li>
      <li class="contact-list__item">
        <svg class="contact-list__icon" viewBox="0 0 24 24" fill="none" stroke="#ffffff" stroke-width="1.4" aria-hidden="true">
          <circle cx="12" cy="12" r="10"/>
          <ellipse cx="12" cy="12" rx="4.5" ry="10"/>
          <path d="M2 12h20"/>
        </svg>
        www.emberre.com
      </li>
      <li class="contact-list__item">
        <svg class="contact-list__icon" viewBox="0 0 24 24" fill="none" stroke="#ffffff" stroke-width="1.3" stroke-linejoin="round" aria-hidden="true">
          <path d="M1 11 L23 3 L16 22 L11 13 Z"/>
          <path d="M11 13 L23 3"/>
          <path d="M11 13 L10 20 L13 17"/>
        </svg>
        info@emberre.com
      </li>
      <li class="contact-list__item contact-list__item--address">
        <svg class="contact-list__icon" viewBox="0 0 24 24" fill="none" stroke="#ffffff" stroke-width="1.4" aria-hidden="true">
          <path d="M12 23 C7 16 4.5 12.5 4.5 9 a7.5 7.5 0 0 1 15 0 c0 3.5-2.5 7-7.5 14z"/>
          <circle cx="12" cy="9" r="2.8"/>
        </svg>
        48 Alder Lane Riverton MA 02190
      </li>
    </ul>
  </section>

</main>
</body>
</html>
```